BrightNomadRx.com Blog Design (Travel, Lifestyle, and Life Hacking blog)

I am launching a lifestyle blog about my life. I'm a doctor who travels the world trying the best restaurants, airlines and trying to have as much fun as possible. I also invest in startups, and am always trying new tricks to make life better. I also plan to write about various other topics, but essentially it is about travel, lifestyle and medicine. I need a creative and really awesome looking design for a new wordpress blog called BrightNomadRx

Target Market(s)

Physicians, Entrepreneurs, Travellers

Industry/Entity Type

Airlines

Number of Pages Required

1 page

Font styles to use
Serif

Requirements
Must have
• Slick looking graphics with a highly professional modern feel

```html
<!DOCTYPE html>
<html lang="en">
<head>
<meta charset="utf-8">
<title>BrightNomadRx — Travel, Lifestyle, and Life Hacking blog</title>
<link rel="stylesheet" href="https://fonts.googleapis.com/css2?family=Archivo+Black&family=Lato:wght@400;700;900&display=swap">
<style>
  :root {
    --ink: #1b1b1b;
    --hero-dark: #151515;
    --frame: #2e2e2e;
    --page: #ffffff;
    --card: #f1f1f1;
    --text: #2a2a2a;
    --link: #3a8ee6;
    --band: #f3f3f3;
    --footer: #232323;
    --rule: #777777;
  }
  * { box-sizing: border-box; margin: 0; padding: 0; }
  html, body { width: 1200px; height: 2256px; overflow: hidden; background: var(--page); }
  body { position: relative; font-family: "Lato", Arial, sans-serif; color: var(--text); }

  .hero { position: absolute; left: 0; top: 0; width: 1200px; height: 720px; overflow: hidden; background: var(--frame); }
  .hero svg { position: absolute; inset: 0; }
  .hero-content { position: absolute; left: 300px; top: 270px; width: 600px; text-align: center; color: #fff; }
  .site-name { font-family: "Archivo Black", "Arial Black", sans-serif; font-size: 40px; letter-spacing: 3px; line-height: 44px; }
  .tagline { margin-top: 24px; font-size: 30px; line-height: 44px; letter-spacing: 1.5px; font-weight: 700; }
  .view-more { display: inline-block; margin-top: 33px; width: 242px; height: 58px; border: 2px solid #fff; line-height: 54px; font-size: 19px; letter-spacing: 2px; color: #fff; }

  .posts { position: absolute; left: 162px; top: 782px; display: flex; gap: 15px; align-items: flex-start; }
  .posts-column { width: 280px; display: flex; flex-direction: column; }
  .post { background: var(--card); }
  .post-media { width: 100%; height: var(--h); }
  .post-body { padding: 10px 22px 12px 24px; }
  .post-title { font-size: 17px; line-height: 20px; font-weight: 900; letter-spacing: 1.5px; text-transform: uppercase; color: var(--ink); }
  .post-excerpt { margin-top: 4px; font-size: 13px; line-height: 17px; font-weight: 700; color: #333; }
  .post-meta { margin-top: 10px; display: flex; justify-content: space-between; align-items: center; }
  .read-more { border: 2px solid #333; padding: 1px 7px; font-size: 13px; font-weight: 700; letter-spacing: 0.5px; color: #333; }
  .comments { font-size: 13px; color: var(--link); letter-spacing: 0.8px; margin-right: 6px; }

  .load-more { position: absolute; left: 162px; top: 1937px; width: 242px; height: 60px; border: 2px solid var(--ink); text-align: center; line-height: 56px; font-size: 19px; letter-spacing: 2.5px; font-weight: 700; color: var(--ink); }

  .subscribe { position: absolute; left: 0; top: 2046px; width: 1200px; height: 137px; background: var(--band); border-top: 5px solid #2d2d2d; }
  .subscribe-label { position: absolute; left: 97px; top: 52px; font-size: 15px; line-height: 26px; font-weight: 900; letter-spacing: 1px; color: #444; text-transform: uppercase; }
  .email-field { position: absolute; left: 445px; top: 54px; width: 308px; height: 43px; border: 1.5px solid var(--rule); background: #fff; font-size: 11px; letter-spacing: 1px; color: #777; padding-left: 22px; line-height: 40px; }
  .email-field svg { position: absolute; right: 12px; top: 13px; }
  .social { position: absolute; left: 792px; top: 54px; display: flex; border: 1.5px solid var(--rule); }
  .social-cell { width: 49.5px; height: 40px; border-left: 1.5px solid var(--rule); display: flex; align-items: center; justify-content: center; }
  .social-cell:first-child { border-left: none; }
  .social-mark { width: 9px; height: 9px; background: #777; }

  .site-footer { position: absolute; left: 0; top: 2183px; width: 1200px; height: 73px; background: var(--footer); color: #fff; font-size: 15px; font-weight: 700; letter-spacing: 0.5px; }
  .copyright { position: absolute; left: 97px; top: 26px; }
  .legal { position: absolute; right: 108px; top: 22px; display: flex; align-items: center; gap: 16px; }
  .legal .divider { width: 2px; height: 26px; background: #bbb; }
</style>
</head>
<body>

<header class="hero">
  <svg width="1200" height="720" viewBox="0 0 1200 720" xmlns="http://www.w3.org/2000/svg">
    <defs>
      <linearGradient id="sky-landmarks" x1="0" y1="0" x2="0.4" y2="1"><stop offset="0" stop-color="#62b6ec"/><stop offset="0.55" stop-color="#9fd0ee"/><stop offset="0.8" stop-color="#b98a5a"/><stop offset="1" stop-color="#2f86b8"/></linearGradient>
      <linearGradient id="cheer-sky" x1="0" y1="0" x2="1" y2="1"><stop offset="0" stop-color="#4a9be0"/><stop offset="0.6" stop-color="#f0e6e0"/><stop offset="1" stop-color="#d2482e"/></linearGradient>
      <linearGradient id="mountain-view" x1="0" y1="0" x2="0" y2="1"><stop offset="0" stop-color="#d7e8f1"/><stop offset="0.5" stop-color="#9fb3b6"/><stop offset="0.75" stop-color="#6f8a6a"/><stop offset="1" stop-color="#3f5e2f"/></linearGradient>
      <linearGradient id="sea-kayak" x1="0" y1="0" x2="0" y2="1"><stop offset="0" stop-color="#c9dfea"/><stop offset="0.45" stop-color="#8fb8cc"/><stop offset="0.75" stop-color="#d9b23a"/><stop offset="1" stop-color="#3f7f98"/></linearGradient>
      <linearGradient id="tubes" x1="0" y1="0" x2="1" y2="1"><stop offset="0" stop-color="#2e2926"/><stop offset="0.5" stop-color="#7d6650"/><stop offset="1" stop-color="#c0a585"/></linearGradient>
      <linearGradient id="flat-icons" x1="0" y1="0" x2="1" y2="1"><stop offset="0" stop-color="#b3dce4"/><stop offset="0.7" stop-color="#9ccfd9"/><stop offset="1" stop-color="#5d8fa6"/></linearGradient>
    </defs>
    <polygon role="img" aria-label="Travel landmarks rising from the sea under a blue sky with a plane and balloons" points="0,0 600,0 225,360 0,144" fill="url(#sky-landmarks)"/>
    <polygon role="img" aria-label="Woman and child cheering with arms spread" points="0,144 225,360 0,576" fill="url(#cheer-sky)"/>
    <polygon role="img" aria-label="Traveller with arms open above a green mountain valley" points="0,576 225,360 600,720 0,720" fill="url(#mountain-view)"/>
    <polygon role="img" aria-label="Woman paddling a yellow kayak on a bay" points="600,0 1200,0 1200,144 975,360" fill="url(#sea-kayak)"/>
    <polygon role="img" aria-label="Stacked cardboard tubes seen end on" points="1200,144 975,360 1200,576" fill="url(#tubes)"/>
    <polygon role="img" aria-label="Flat illustration of life tools and a start screen" points="1200,576 975,360 600,720 1200,720" fill="url(#flat-icons)"/>
    <g fill="none" stroke="var(--frame)" stroke-width="20">
      <line x1="600" y1="0" x2="0" y2="576"/>
      <line x1="600" y1="720" x2="0" y2="144"/>
      <line x1="600" y1="0" x2="1200" y2="576"/>
      <line x1="600" y1="720" x2="1200" y2="144"/>
    </g>
    <rect x="0" y="0" width="1200" height="720" fill="none" stroke="var(--frame)" stroke-width="10"/>
    <polygon points="600,6 969,360 600,714 231,360" fill="var(--hero-dark)" stroke="#262626" stroke-width="8"/>
  </svg>
  <div class="hero-content">
    <h1 class="site-name">BrightNomadRx</h1>
    <p class="tagline">Travel, Lifestyle, and Life<br>Hacking blog</p>
    <span class="view-more">VIEW MORE</span>
  </div>
</header>

<main class="posts">
  <div class="posts-column">
    <article class="post" style="margin-bottom:12px">
      <div class="post-media" style="--h:181px;background:linear-gradient(120deg,#e4ddd2 0%,#c7c2b8 30%,#243056 50%,#1d1d28 70%,#4a1a12 100%)" role="img" aria-label="Soda bottle beside a glass of cola"></div>
      <div class="post-body">
        <h2 class="post-title">Life Hacking</h2>
        <p class="post-excerpt">Lorem Ipsum has been the industry's standard dummy text ever since the 1500s, when an unknown printer took a galley of type and scrambled it to make a type specimen book.</p>
        <div class="post-meta"><span class="read-more">Read More</span><span class="comments">0 Comment</span></div>
      </div>
    </article>
    <article class="post" style="margin-bottom:28px">
      <div class="post-media" style="--h:203px;background:linear-gradient(135deg,#48c0ee,#29a3e0 60%,#1b86c6)" role="img" aria-label="Blue news graphic with office icons"></div>
      <div class="post-body">
        <h2 class="post-title">Life Hacking</h2>
        <p class="post-excerpt">Lorem Ipsum has been the industry's standard dummy text ever since the 1500s, when an unknown printer took a galley of type and scrambled it to make a type specimen book.</p>
        <div class="post-meta"><span class="read-more">Read More</span><span class="comments">0 Comment</span></div>
      </div>
    </article>
    <article class="post">
      <div class="post-media" style="--h:185px;background:linear-gradient(160deg,#b7cfa0 0%,#6f8f48 40%,#3d5a2a 65%,#c9443a 100%)" role="img" aria-label="Students with laptops on a lawn"></div>
      <div class="post-body">
        <h2 class="post-title">Life Hacking</h2>
        <p class="post-excerpt">Lorem Ipsum has been the industry's standard dummy text ever since the 1500s, when an unknown printer took a galley of type and scrambled it to make a type specimen book.</p>
        <div class="post-meta"><span class="read-more">Read More</span><span class="comments">0 Comment</span></div>
      </div>
    </article>
  </div>

  <div class="posts-column">
    <article class="post" style="margin-bottom:30px">
      <div class="post-media" style="--h:200px;background:linear-gradient(180deg,#2c6ad0 0%,#6fa6e6 25%,#f2f4f6 50%,#e0d8cc 75%,#a88a66 100%)" role="img" aria-label="White hillside village above a blue sea"></div>
      <div class="post-body">
        <h2 class="post-title">Life Hacking</h2>
        <p class="post-excerpt">Lorem Ipsum has been the industry's standard dummy text ever since the 1500s, when an unknown printer took a galley of type and scrambled it to make a type specimen book.</p>
        <div class="post-meta"><span class="read-more">Read More</span><span class="comments">0 Comment</span></div>
      </div>
    </article>
    <article class="post" style="margin-bottom:12px">
      <div class="post-media" style="--h:187px;background:linear-gradient(180deg,#3f8fdc 0%,#9cc6ee 35%,#f1e6dc 55%,#d24a2e 75%,#2f6a2a 100%)" role="img" aria-label="Woman and child cheering outdoors"></div>
      <div class="post-body">
        <h2 class="post-title">Life Hacking</h2>
        <p class="post-excerpt">Lorem Ipsum has been the industry's standard dummy text ever since the 1500s, when an unknown printer took a galley of type and scrambled it to make a type specimen book.</p>
        <div class="post-meta"><span class="read-more">Read More</span><span class="comments">0 Comment</span></div>
      </div>
    </article>
    <article class="post">
      <div class="post-media" style="--h:205px;background:linear-gradient(180deg,#8ccbec 0%,#46b0d4 45%,#2e9cc0 65%,#c07a62 85%,#a05a48 100%)" role="img" aria-label="Family walking on a seaside pier"></div>
      <div class="post-body">
        <h2 class="post-title">Life Hacking</h2>
        <p class="post-excerpt">Lorem Ipsum has been the industry's standard dummy text ever since the 1500s, when an unknown printer took a galley of type and scrambled it to make a type specimen book.</p>
        <div class="post-meta"><span class="read-more">Read More</span><span class="comments">0 Comment</span></div>
      </div>
    </article>
  </div>

  <div class="posts-column" style="margin-top:2px">
    <article class="post" style="margin-bottom:5px">
      <div class="post-media" style="--h:196px;background:linear-gradient(180deg,#8cc2ee 0%,#bcdaf0 40%,#3ea5c4 60%,#e6dccb 85%,#d6c2a0 100%)" role="img" aria-label="Family running along a sunny beach"></div>
      <div class="post-body">
        <h2 class="post-title">Life Hacking</h2>
        <p class="post-excerpt">Lorem Ipsum has been the industry's standard dummy text ever since the 1500s, when an unknown printer took a galley of type.</p>
        <div class="post-meta"><span class="read-more">Read More</span><span class="comments">0 Comment</span></div>
      </div>
    </article>
    <article class="post" style="margin-bottom:15px">
      <div class="post-media" style="--h:182px;background:linear-gradient(180deg,#2376c2 0%,#3aa0d2 35%,#48c0c4 55%,#b9c79a 75%,#c9c2ae 100%)" role="img" aria-label="Vintage van parked under palm trees by the sea"></div>
      <div class="post-body">
        <h2 class="post-title">Life Hacking</h2>
        <p class="post-excerpt">Lorem Ipsum has been the industry's standard dummy text ever since the 1500s, when an unknown printer took a galley of type and scrambled it to make a type specimen book.</p>
        <div class="post-meta"><span class="read-more">Read More</span><span class="comments">0 Comment</span></div>
      </div>
    </article>
    <article class="post">
      <div class="post-media" style="--h:200px;background:linear-gradient(135deg,#b4dde5,#9ccfd9 60%,#86c0cc)" role="img" aria-label="Flat illustration of life tools around a start screen"></div>
      <div class="post-body">
        <h2 class="post-title">Life Hacking</h2>
        <p class="post-excerpt">Lorem Ipsum has been the industry's standard dummy text ever since the 1500s, when an unknown printer took a galley of type and scrambled it to make a type specimen book.</p>
        <div class="post-meta"><span class="read-more">Read More</span><span class="comments">0 Comment</span></div>
      </div>
    </article>
  </div>
</main>

<span class="load-more">LOAD MORE</span>

<section class="subscribe">
  <p class="subscribe-label">Subscribe to latest smartphones<br>news &amp; great deals we offer</p>
  <div class="email-field">ENTER YOUR EMAIL ADDRESS ...
    <svg width="16" height="13" viewBox="0 0 16 13"><rect x="1" y="1" width="14" height="11" fill="none" stroke="#666" stroke-width="1.5"/><polyline points="1,1 8,7 15,1" fill="none" stroke="#666" stroke-width="1.5"/></svg>
  </div>
  <div class="social" aria-label="Social links">
    <span class="social-cell"><span class="social-mark"></span></span>
    <span class="social-cell"><span class="social-mark"></span></span>
    <span class="social-cell"><span class="social-mark"></span></span>
    <span class="social-cell"><span class="social-mark"></span></span>
    <span class="social-cell"><span class="social-mark"></span></span>
    <span class="social-cell"><span class="social-mark"></span></span>
  </div>
</section>

<footer class="site-footer">
  <p class="copyright">Bright Nomad Rx 2016.</p>
  <nav class="legal"><span>Terms &amp; Conditions</span><span class="divider"></span><span>Privacy Policy</span></nav>
</footer>

</body>
</html>
```